Website transfer and revamp for consultancy

We are a professional management consultancy and need our current website transferred and modernised from Wix to WordPress with the most efficient SEO updates and blog included. We are open for options of new site set up.

Website must be relatively easy for us to maintain and update ourselves.

Website must also be desktop/mobile/ipad friendly.

www.velmora-advisory-partners.com

Target Market(s)

General manufacturers, construction, developers, oil and gas

Industry/Entity Type

Management Consulting

Font styles to use
Serif

Colors

Designer to choose colors to be used in the design.

Requirements
Must have
• Must have same bulk content as the existing website as a minimum with the addition of a blog page. We are open to added content.
Nice to have
• Open to designer additions such as "projects completed" and "value created" number generators
• .
Should not have
• DO NOT USE stock photos which are not free for use to use.

```html
<!DOCTYPE html>
<html lang="en">
<head>
<meta charset="utf-8">
<title>Velmora Advisory – The Contract and Conflict Advisory</title>
<link rel="stylesheet" href="https://fonts.googleapis.com/css2?family=Cinzel:wght@400;700&family=Open+Sans:wght@400;600;700&display=swap">
<style>
:root{
  --navy:#1c3d5e;
  --navy-deep:#1b2b52;
  --red:#c0192e;
  --ink:#222;
  --muted:#777;
  --line:#e3e3e3;
  --white:#fff;
  --serif:'Cinzel',serif;
  --sans:'Open Sans',sans-serif;
}
*{box-sizing:border-box;margin:0;padding:0}
html,body{width:1200px;height:2980px;overflow:hidden}
body{font-family:var(--sans);color:var(--ink);background:var(--white);position:relative}
a{color:inherit;text-decoration:none}

/* Header */
.site-header{position:absolute;top:0;left:0;width:1200px;height:130px;background:var(--white)}
.brand{position:absolute;left:100px;top:40px;display:flex;align-items:center;gap:12px}
.brand-dot{width:34px;height:34px;border-radius:50%;background:var(--navy)}
.brand-name{font-family:var(--serif);font-weight:700;font-size:24px;color:var(--navy);line-height:1;white-space:nowrap}
.brand-tag{font-family:var(--serif);font-size:9px;color:var(--navy);letter-spacing:.5px;margin-top:5px;white-space:nowrap}
.header-actions{position:absolute;right:100px;top:24px;display:flex;gap:10px}
.pill{height:42px;border-radius:21px;padding:0 18px;display:flex;align-items:center;font-size:13px;font-weight:700;color:var(--white);text-transform:uppercase}
.pill-navy{background:var(--navy)}
.pill-red{background:var(--red);padding:0 34px}
.main-nav{position:absolute;left:360px;top:90px;display:flex;gap:34px;font-family:var(--serif);font-size:13px;color:var(--navy)}
.main-nav .active{font-weight:700;border-top:2px solid var(--red);padding-top:2px;margin-top:-4px}
.search-icon{position:absolute;right:100px;top:92px}

/* Hero */
.hero{position:absolute;top:130px;left:0;width:1200px;height:640px;overflow:hidden}
.hero-photo{position:absolute;inset:0;background:linear-gradient(180deg,#3d5f93 0%,#7187b0 35%,#c58a6a 60%,#3a3838 85%)}
.hero-title{position:absolute;top:230px;width:100%;text-align:center;color:var(--white);font-family:var(--serif)}
.hero-title h1{font-size:60px;font-weight:700;letter-spacing:2px}
.hero-title .tag{font-size:20px;margin-top:12px;letter-spacing:1px}
.hero-title .regions{font-size:13px;margin-top:14px;letter-spacing:.5px}
.hero-arrow{position:absolute;top:250px;width:36px;height:36px;background:rgba(0,0,0,.45);display:flex;align-items:center;justify-content:center}
.hero-wave{position:absolute;left:0;bottom:0}
.stat-ring{position:absolute;left:530px;top:425px;width:140px;height:140px}
.stat-ring span{position:absolute;inset:0;display:flex;align-items:center;justify-content:center;font-weight:700;font-size:34px;color:var(--red)}
.stat-ring small{font-size:16px;margin-top:8px}
.stat-caption{position:absolute;top:582px;width:100%;text-align:center;color:var(--white);font-size:15px;line-height:22px}

/* Welcome */
.welcome{position:absolute;top:770px;left:0;width:1200px;height:495px;text-align:center}
.section-title{font-family:var(--serif);font-weight:400;font-size:31px;color:var(--navy-deep);letter-spacing:.5px}
.welcome .section-title{margin-top:64px}
.welcome p{width:560px;margin:18px auto 0;font-size:14px;line-height:24px;color:var(--muted)}
.sectors{position:absolute;top:210px;left:100px;width:1000px;display:flex;justify-content:space-between}
.sector{width:250px;text-align:center}
.sector svg{display:block;margin:0 auto}
.sector h3{font-weight:400;font-size:16px;line-height:24px;margin-top:20px;color:var(--ink)}

/* Advisory */
.advisory{position:absolute;top:1265px;left:0;width:1200px;height:447px;display:flex}
.advisory-col{width:600px;height:447px;padding:58px 0 0 100px;color:var(--white)}
.advisory-col.conflict{background:linear-gradient(90deg,#244c6c,#1d4465)}
.advisory-col.contract{background:linear-gradient(90deg,#1e2d58,#1b2a52);padding-left:125px}
.advisory-col h2{font-family:var(--serif);font-weight:400;font-size:31px;letter-spacing:.5px}
.advisory-col ul{list-style:none;margin-top:26px;width:330px}
.advisory-col li{position:relative;padding-left:28px;font-size:14px;line-height:22px;margin-bottom:23px}
.advisory-col li svg{position:absolute;left:0;top:3px}
.btn-outline{display:inline-block;margin-top:2px;border:2px solid var(--white);border-radius:22px;padding:10px 22px;font-size:13px;font-weight:700}
.advisory-badge{position:absolute;left:547px;top:172px;width:106px;height:106px;border-radius:50%;background:var(--white);display:flex;align-items:center;justify-content:center;font-family:var(--serif);font-weight:700;font-size:15px;color:var(--navy)}

/* Blog */
.blog{position:absolute;top:1712px;left:0;width:1200px;height:628px;text-align:center}
.blog .section-title{margin-top:82px}
.posts{position:absolute;top:158px;left:100px;width:1002px;display:flex;justify-content:space-between;text-align:left}
.post{width:322px}
.post-photo{height:210px}
.post h3{font-weight:600;font-size:18px;margin-top:36px}
.post-meta{display:flex;align-items:center;gap:6px;font-size:12px;color:var(--muted);margin-top:10px}
.post p{font-size:12px;line-height:20px;color:#555;margin-top:12px}
.read-more{display:block;margin-top:14px;font-size:13px;font-weight:700;color:var(--red)}

/* Stats */
.stats{position:absolute;top:2340px;left:0;width:1200px;height:268px}
.stats-photo{position:absolute;inset:0;background:linear-gradient(90deg,#2b2622 0%,#6a5a4d 35%,#c99168 65%,#e5a46a 100%)}
.stat{position:absolute;top:58px;display:flex;align-items:center;color:var(--white)}
.stat-circle{width:154px;height:154px;border:2px solid var(--white);border-radius:50%;display:flex;align-items:center;justify-content:center}
.stat-text{margin-left:26px;margin-top:-20px}
.stat-num{font-weight:700;font-size:44px;line-height:1}
.stat-label{font-family:var(--serif);font-size:23px;margin-top:14px}

/* Footer */
.site-footer{position:absolute;top:2608px;left:0;width:1200px;height:372px}
.footer-brand{position:absolute;left:100px;top:100px;text-align:center;width:260px}
.footer-brand .brand-dot{margin:0 auto 10px;width:40px;height:40px}
.footer-brand .brand-name{font-size:22px}
.footer-col{position:absolute;top:82px}
.footer-col h4{font-family:var(--serif);font-weight:400;font-size:18px;color:var(--ink);margin-bottom:20px;white-space:nowrap}
.quick-links{left:402px}
.quick-links li{list-style:none;font-size:12px;line-height:25px;color:#444}
.newsletter{left:572px;width:260px}
.newsletter p{font-size:12px;line-height:20px;color:#555;width:200px}
.newsletter .field{border-bottom:1px solid #ccc;font-size:11px;color:#999;padding:12px 0 6px 4px;margin-top:6px;width:252px}
.newsletter .subscribe{display:inline-block;margin-top:14px;background:var(--red);color:var(--white);font-size:11px;font-weight:700;border-radius:15px;padding:7px 18px}
.contact{left:876px;width:280px}
.contact li{list-style:none;display:flex;gap:14px;font-size:11px;line-height:18px;color:#444;margin-bottom:16px;white-space:nowrap}
.contact li svg{flex:none;margin-top:3px}
.footer-bottom{position:absolute;left:100px;top:290px;width:1002px;border-top:1px solid var(--line);padding-top:28px;font-size:11px;color:#555}
.socials{position:absolute;right:0;top:20px;display:flex;gap:8px}
.socials span{width:24px;height:24px;border:1px solid var(--red);border-radius:50%}
</style>
</head>
<body>

<header class="site-header">
  <a class="brand" href="#">
    <span class="brand-dot"></span>
    <span><span class="brand-name">Velmora Advisory</span><div class="brand-tag">THE CONTRACT AND CONFLICT ADVISORY</div></span>
  </a>
  <div class="header-actions">
    <a class="pill pill-navy" href="#">Arrange a Consultation</a>
    <a class="pill pill-red" href="#">Brochure</a>
  </div>
  <nav class="main-nav">
    <a class="active" href="#">HOME</a><a href="#">ABOUT US</a><a href="#">CONFLICT ADVISORY</a><a href="#">CONTRACT ADVISORY</a><a href="#">BLOG</a><a href="#">CONTACT US</a>
  </nav>
  <svg class="search-icon" width="14" height="14" viewBox="0 0 14 14"><circle cx="6" cy="6" r="4.5" fill="none" stroke="#1c3d5e" stroke-width="2"/><path d="M9.5 9.5L13 13" stroke="#1c3d5e" stroke-width="2"/></svg>
</header>

<section class="hero">
  <div class="hero-photo" role="img" aria-label="City skyline at dusk with office towers beside a river"></div>
  <div class="hero-title">
    <h1>VELMORA ADVISORY</h1>
    <div class="tag">THE CONTRACT AND CONFLICT ADVISORY</div>
    <div class="regions">UNITED KINGDOM &nbsp;•&nbsp; IRELAND &nbsp;•&nbsp; UNITED ARAB EMIRATES</div>
  </div>
  <div class="hero-arrow" style="left:0"><svg width="10" height="14"><path d="M8 1L2 7l6 6" fill="none" stroke="#fff" stroke-width="2"/></svg></div>
  <div class="hero-arrow" style="right:0"><svg width="10" height="14"><path d="M2 1l6 6-6 6" fill="none" stroke="#fff" stroke-width="2"/></svg></div>
  <svg class="hero-wave" width="1200" height="230" viewBox="0 0 1200 230"><path d="M0 60 Q600 -40 1200 60 L1200 230 L0 230Z" fill="#c0192e"/></svg>
  <div class="stat-ring">
    <svg width="140" height="140" viewBox="0 0 140 140"><circle cx="70" cy="70" r="68" fill="#fff"/><circle cx="70" cy="70" r="58" fill="none" stroke="#c0192e" stroke-width="4"/><path d="M70 12 A58 58 0 0 1 105 24" fill="none" stroke="#1c3d5e" stroke-width="4"/></svg>
    <span>9<small>%</small></span>
  </div>
  <div class="stat-caption">The average revenue lost from<br>inadequate contract management</div>
</section>

<section class="welcome">
  <h2 class="section-title">Welcome to Velmora Advisory</h2>
  <p>We are an experienced contract and conflict advisory providing global contract performance solutions and conflict manage-ment to:</p>
  <div class="sectors">
    <div class="sector">
      <svg width="150" height="150" viewBox="0 0 150 150"><circle cx="75" cy="75" r="70" fill="none" stroke="#1c3d5e" stroke-width="2"/><circle cx="75" cy="75" r="24" fill="none" stroke="#1c3d5e" stroke-width="4"/><path d="M51 75h48M75 51c-10 12-10 36 0 48M75 51c10 12 10 36 0 48" fill="none" stroke="#1c3d5e" stroke-width="3"/></svg>
      <h3>International development<br>organisations</h3>
    </div>
    <div class="sector">
      <svg width="150" height="150" viewBox="0 0 150 150"><circle cx="75" cy="75" r="70" fill="none" stroke="#1c3d5e" stroke-width="2"/><rect x="60" y="50" width="30" height="50" fill="#1c3d5e"/><path d="M66 58h6v6h-6zM78 58h6v6h-6zM66 70h6v6h-6zM78 70h6v6h-6zM66 82h6v6h-6zM78 82h6v6h-6z" fill="#fff"/></svg>
      <h3>Construction industry</h3>
    </div>
    <div class="sector">
      <svg width="150" height="150" viewBox="0 0 150 150"><circle cx="75" cy="75" r="70" fill="none" stroke="#1c3d5e" stroke-width="2"/><path d="M75 50 C67 66 60 74 60 84 a15 15 0 0 0 30 0 c0-10-7-18-15-34z" fill="#1c3d5e"/></svg>
      <h3>Oil and gas industry</h3>
    </div>
    <div class="sector">
      <svg width="150" height="150" viewBox="0 0 150 150"><circle cx="75" cy="75" r="70" fill="none" stroke="#1c3d5e" stroke-width="2"/><path d="M53 64 L75 51 L97 64Z M57 68h6v22h-6z M72 68h6v22h-6z M87 68h6v22h-6z M52 93h46v5H52z" fill="#1c3d5e"/></svg>
      <h3>Government sectors</h3>
    </div>
  </div>
</section>

<section class="advisory">
  <div class="advisory-col conflict">
    <h2>CONFLICT ADVISORY</h2>
    <ul>
      <li><svg width="15" height="15"><circle cx="7.5" cy="7.5" r="7.5" fill="#fff"/><path d="M4 7.5l2.5 2.5 4.5-5" fill="none" stroke="#1d4465" stroke-width="2"/></svg>Restoration and Mediation Services</li>
      <li><svg width="15" height="15"><circle cx="7.5" cy="7.5" r="7.5" fill="#fff"/><path d="M4 7.5l2.5 2.5 4.5-5" fill="none" stroke="#1d4465" stroke-width="2"/></svg>Shuttle Diplomacy Services and In Personal Intermediary Services</li>
      <li><svg width="15" height="15"><circle cx="7.5" cy="7.5" r="7.5" fill="#fff"/><path d="M4 7.5l2.5 2.5 4.5-5" fill="none" stroke="#1d4465" stroke-width="2"/></svg>Negotiation Support Services</li>
      <li><svg width="15" height="15"><circle cx="7.5" cy="7.5" r="7.5" fill="#fff"/><path d="M4 7.5l2.5 2.5 4.5-5" fill="none" stroke="#1d4465" stroke-width="2"/></svg>Workplace Mediation Services</li>
    </ul>
    <a class="btn-outline" href="#">READ MORE</a>
  </div>
  <div class="advisory-col contract">
    <h2>CONTRACT ADVISORY</h2>
    <ul>
      <li><svg width="15" height="15"><circle cx="7.5" cy="7.5" r="7.5" fill="#fff"/><path d="M4 7.5l2.5 2.5 4.5-5" fill="none" stroke="#1b2a52" stroke-width="2"/></svg>Contract Troubleshooting</li>
      <li><svg width="15" height="15"><circle cx="7.5" cy="7.5" r="7.5" fill="#fff"/><path d="M4 7.5l2.5 2.5 4.5-5" fill="none" stroke="#1b2a52" stroke-width="2"/></svg>Contracts Audit Services and Performance Management</li>
      <li><svg width="15" height="15"><circle cx="7.5" cy="7.5" r="7.5" fill="#fff"/><path d="M4 7.5l2.5 2.5 4.5-5" fill="none" stroke="#1b2a52" stroke-width="2"/></svg>Strategic Review &amp; Risk Assessment</li>
      <li><svg width="15" height="15"><circle cx="7.5" cy="7.5" r="7.5" fill="#fff"/><path d="M4 7.5l2.5 2.5 4.5-5" fill="none" stroke="#1b2a52" stroke-width="2"/></svg>Contract Fraud Investigation</li>
    </ul>
    <a class="btn-outline" href="#">READ MORE</a>
  </div>
  <div class="advisory-badge">VELMORA</div>
</section>

<section class="blog">
  <h2 class="section-title">Latest Blog</h2>
  <div class="posts">
    <article class="post">
      <div class="post-photo" role="img" aria-label="Business colleagues talking in a bright office" style="background:linear-gradient(135deg,#d9dde2,#8a8f96 60%,#3a3d44)"></div>
      <h3>Finibus Bonorum et Malorum</h3>
      <div class="post-meta"><svg width="11" height="11"><rect x="0.5" y="1.5" width="10" height="9" fill="#c0192e"/></svg>25/09/2017 &nbsp;|&nbsp; <svg width="10" height="11"><circle cx="5" cy="3" r="3" fill="#1c3d5e"/><path d="M0 11a5 5 0 0 1 10 0z" fill="#1c3d5e"/></svg>Daniel</div>
      <p>Nemo enim ipsam voluptatem quia volupta asperna tur aut odit aut fugit, sed quia conseq.</p>
      <a class="read-more" href="#">READ MORE</a>
    </article>
    <article class="post">
      <div class="post-photo" role="img" aria-label="Hands signing a contract on a desk" style="background:linear-gradient(135deg,#eeeae6,#c8c2bc 55%,#7d8391)"></div>
      <h3>Finibus Bonorum et Malorum</h3>
      <div class="post-meta"><svg width="11" height="11"><rect x="0.5" y="1.5" width="10" height="9" fill="#c0192e"/></svg>25/09/2017 &nbsp;|&nbsp; <svg width="10" height="11"><circle cx="5" cy="3" r="3" fill="#1c3d5e"/><path d="M0 11a5 5 0 0 1 10 0z" fill="#1c3d5e"/></svg>Daniel</div>
      <p>Nemo enim ipsam voluptatem quia volupta asperna tur aut odit aut fugit, sed quia conseq.</p>
      <a class="read-more" href="#">READ MORE</a>
    </article>
    <article class="post">
      <div class="post-photo" role="img" aria-label="Advisors meeting with clients at a table" style="background:linear-gradient(135deg,#f0ece4,#d7b89a 50%,#b2604a)"></div>
      <h3>Finibus Bonorum et Malorum</h3>
      <div class="post-meta"><svg width="11" height="11"><rect x="0.5" y="1.5" width="10" height="9" fill="#c0192e"/></svg>25/09/2017 &nbsp;|&nbsp; <svg width="10" height="11"><circle cx="5" cy="3" r="3" fill="#1c3d5e"/><path d="M0 11a5 5 0 0 1 10 0z" fill="#1c3d5e"/></svg>Daniel</div>
      <p>Nemo enim ipsam voluptatem quia volupta asperna tur aut odit aut fugit, sed quia conseq.</p>
      <a class="read-more" href="#">READ MORE</a>
    </article>
  </div>
</section>

<section class="stats">
  <div class="stats-photo" role="img" aria-label="Two business people shaking hands in warm light"></div>
  <div class="stat" style="left:100px">
    <div class="stat-circle"><svg width="60" height="52" viewBox="0 0 60 52"><circle cx="22" cy="30" r="14" fill="none" stroke="#fff" stroke-width="8" stroke-dasharray="5 4"/><circle cx="22" cy="30" r="6" fill="#fff"/><circle cx="45" cy="12" r="8" fill="none" stroke="#fff" stroke-width="5" stroke-dasharray="3 3"/></svg></div>
    <div class="stat-text"><div class="stat-num">125830</div><div class="stat-label">PROJECTS COMPLETED</div></div>
  </div>
  <div class="stat" style="left:665px">
    <div class="stat-circle"><svg width="54" height="54" viewBox="0 0 54 54"><circle cx="27" cy="27" r="25" fill="#fff"/><path d="M15 27l8 8 16-16" fill="none" stroke="#a86a44" stroke-width="6"/></svg></div>
    <div class="stat-text"><div class="stat-num">125830</div><div class="stat-label">VALUE CREATED</div></div>
  </div>
</section>

<footer class="site-footer">
  <div class="footer-brand">
    <div class="brand-dot"></div>
    <div class="brand-name">Velmora Advisory</div>
    <div class="brand-tag">THE CONTRACT AND CONFLICT ADVISORY</div>
  </div>
  <div class="footer-col quick-links">
    <h4>Quick Links</h4>
    <ul><li>Home</li><li>About Us</li><li>Conflict Advisory</li><li>Contract Advisory</li><li>Blog</li><li>Contact Us</li></ul>
  </div>
  <div class="footer-col newsletter">
    <h4>Newsletter Subscription</h4>
    <p>Register your Email Address to get information about us</p>
    <div class="field">Email Address</div>
    <span class="subscribe">SUBSCRIBE</span>
  </div>
  <div class="footer-col contact">
    <h4>Contact Us</h4>
    <ul>
      <li><svg width="10" height="14"><path d="M5 0a5 5 0 0 1 5 5c0 4-5 9-5 9S0 9 0 5a5 5 0 0 1 5-5z" fill="#c0192e"/><circle cx="5" cy="5" r="2" fill="#fff"/></svg><span>Suite 4, 2nd Floor,<br>Halden Court, 27-29 Mercer Lane,<br>Harbour District, Eastbridge, EB4 7QN</span></li>
      <li><svg width="12" height="12"><path d="M2 0l3 3-1.5 2a8 8 0 0 0 3.5 3.5L9 7l3 3-2 2C5 12 0 7 0 2z" fill="#c0192e"/></svg><span>1 555 014 2290</span></li>
      <li><svg width="13" height="10"><rect width="13" height="10" fill="#c0192e"/><path d="M0 0l6.5 5L13 0" fill="none" stroke="#fff"/></svg><span>hello@velmora-advisory-partners.com</span></li>
    </ul>
  </div>
  <div class="footer-bottom">
    Copyrights © 2018, Velmora-advisory-partners.com. All rights reserved.
    <div class="socials"><span></span><span></span><span></span><span></span></div>
  </div>
</footer>

</body>
</html>
```